Tidal Sparks - Main Menu - Re-Design

I want to have a refresh for this app's main menu. There are some different items on the menu depending on the language (English vs. Non-English) and version (Pro vs. Free). I have attached screenshots of the different conditions. This app is a collection of brain training games.

Need designs for light and dark mode. Need designs for both portrait and landscape mode.

Here is a link to the app in Brisk Market.
https://apps.briskmarket.example/store/apps/details?id=tidalworks.tidalsparks

Here is a link to the app in the Orvel App Store.
https://depot.orvel.example/us/app/tidal-sparks-focus-drills/id519274063?ls=1&mt=8

```html
<!DOCTYPE html>
<html lang="en">
<head>
<meta charset="utf-8">
<title>Tidal Sparks – Main Menu</title>
<link rel="stylesheet" href="https://fonts.googleapis.com/css2?family=Poppins:wght@300;400;500;600&display=swap">
<style>
  :root {
    --bg: #f3f1f6;
    --ink: #24222b;
    --ink-soft: #8a8791;
    --divider: #e2e0e6;
    --toggle-track: #e6e4ea;
    --toggle-knob: #ffffff;
    --avatar: #7fa9d3;
    --badge: #0f5f8c;
    --games: #7ba7d1;
    --training: #b39ddb;
    --learning: #e99395;
    --scores: #e8d098;
    --schedule: #9ba6e0;
    --about: #eeb8d5;
    --white: #ffffff;
  }
  * { box-sizing: border-box; margin: 0; padding: 0; }
  html, body {
    width: 1200px; height: 3417px; overflow: hidden;
    background: var(--bg);
    font-family: "Poppins", sans-serif;
  }
  .screen { position: relative; width: 1200px; height: 3417px; }

  .greeting { position: absolute; left: 67px; top: 132px; }
  .greeting__hello { font-size: 43px; font-weight: 300; color: var(--ink-soft); line-height: 1.2; }
  .greeting__name { font-size: 58px; font-weight: 600; color: var(--ink); line-height: 1.3; margin-top: 6px; }

  .theme-toggle {
    position: absolute; left: 67px; top: 313px; width: 133px; height: 58px;
    border-radius: 29px; background: var(--toggle-track);
  }
  .theme-toggle__knob {
    position: absolute; left: 5px; top: 5px; width: 48px; height: 48px; border-radius: 50%;
    background: var(--toggle-knob); box-shadow: 0 2px 6px rgba(0,0,0,.15);
  }

  .avatar {
    position: absolute; left: 948px; top: 168px; width: 186px; height: 186px; border-radius: 50%;
    background: radial-gradient(circle at 50% 40%, #8db4da, var(--avatar));
  }
  .avatar__settings {
    position: absolute; left: 927px; top: 287px; width: 64px; height: 64px;
  }

  .divider { position: absolute; left: 67px; top: 422px; width: 1066px; height: 3px; background: var(--divider); }

  .menu-card {
    position: absolute; left: 67px; width: 1066px; height: 377px; border-radius: 40px;
    color: var(--white);
  }
  .menu-card__title {
    position: absolute; left: 58px; top: 112px; font-size: 70px; font-weight: 500;
    letter-spacing: 4px; line-height: 1;
  }
  .menu-card__subtitle {
    position: absolute; left: 58px; top: 207px; font-size: 36px; font-weight: 300; line-height: 1;
  }
  .menu-card__art {
    position: absolute; right: 30px; top: 58px; width: 360px; height: 260px; border-radius: 36px;
    background: radial-gradient(ellipse at center, rgba(255,255,255,.35), rgba(255,255,255,0) 70%);
  }

  .menu-card--games    { top: 499px;  background: var(--games);    box-shadow: 0 40px 60px -20px rgba(123,167,209,.55); }
  .menu-card--training { top: 986px;  background: var(--training); box-shadow: 0 40px 60px -20px rgba(179,157,219,.55); }
  .menu-card--learning { top: 1458px; background: var(--learning); box-shadow: 0 40px 60px -20px rgba(233,147,149,.55); }
  .menu-card--scores   { top: 1930px; background: var(--scores);   box-shadow: 0 40px 60px -20px rgba(232,208,152,.6); }
  .menu-card--schedule { top: 2403px; background: var(--schedule); box-shadow: 0 40px 60px -20px rgba(155,166,224,.55); }
  .menu-card--about    { top: 2875px; background: var(--about);    box-shadow: 0 40px 60px -20px rgba(238,184,213,.6); }
</style>
</head>
<body>
<main class="screen">
  <header>
    <div class="greeting">
      <p class="greeting__hello">Welcome back,</p>
      <p class="greeting__name">Guest</p>
    </div>
    <div class="theme-toggle" aria-label="Dark mode toggle"><span class="theme-toggle__knob"></span></div>
    <div class="avatar" role="img" aria-label="User avatar illustration"></div>
    <svg class="avatar__settings" viewBox="0 0 64 64" aria-label="Settings">
      <circle cx="32" cy="32" r="30" fill="#ffffff"/>
      <circle cx="32" cy="32" r="26" fill="var(--badge)"/>
      <g fill="#ffffff">
        <rect x="29" y="15" width="6" height="34" rx="2"/>
        <rect x="29" y="15" width="6" height="34" rx="2" transform="rotate(45 32 32)"/>
        <rect x="29" y="15" width="6" height="34" rx="2" transform="rotate(90 32 32)"/>
        <rect x="29" y="15" width="6" height="34" rx="2" transform="rotate(135 32 32)"/>
        <circle cx="32" cy="32" r="12"/>
      </g>
      <circle cx="32" cy="32" r="5" fill="var(--badge)"/>
    </svg>
  </header>
  <div class="divider"></div>

  <nav>
    <a class="menu-card menu-card--games">
      <span class="menu-card__title">GAME LIST</span>
      <span class="menu-card__subtitle">Exercise your brain memory</span>
      <span class="menu-card__art" role="img" aria-label="3D game controller and headphones"></span>
    </a>
    <a class="menu-card menu-card--training">
      <span class="menu-card__title">TRAINING CENTRE</span>
      <span class="menu-card__subtitle">Exercise regularly</span>
      <span class="menu-card__art" role="img" aria-label="3D clipboard with checkmark"></span>
    </a>
    <a class="menu-card menu-card--learning">
      <span class="menu-card__title">LEARNING</span>
      <span class="menu-card__subtitle">Find lots of learning</span>
      <span class="menu-card__art" role="img" aria-label="3D cloud with light bulbs"></span>
    </a>
    <a class="menu-card menu-card--scores">
      <span class="menu-card__title">SCORES</span>
      <span class="menu-card__subtitle">Find the top score here</span>
      <span class="menu-card__art" role="img" aria-label="3D trophies on a podium"></span>
    </a>
    <a class="menu-card menu-card--schedule">
      <span class="menu-card__title">SCHEDULE</span>
      <span class="menu-card__subtitle">Set your schedule</span>
      <span class="menu-card__art" role="img" aria-label="3D desk calendar"></span>
    </a>
    <a class="menu-card menu-card--about">
      <span class="menu-card__title">ABOUT</span>
      <span class="menu-card__subtitle">More info about us</span>
      <span class="menu-card__art" role="img" aria-label="3D little house"></span>
    </a>
  </nav>
</main>
</body>
</html>
```